Business Card Design - cloud video monitoring

For the trade show in Las Vegas our company needs business cards with new brand - Vyrolux

The logo of the new brand is attached, the sample card with the founder's contact details is attached (just change the website to www.vyrolux.me) and email to info@vyrolux.me
Updates

                                        Forgot to say: the tagline for the brand is "the new normal cloud video management"

Industry/Entity Type

Business

```html
<!DOCTYPE html>
<html lang="en">
<head>
<meta charset="utf-8">
<title>Vyrolux — Business Card</title>
<link rel="stylesheet" href="https://fonts.googleapis.com/css2?family=Arimo:wght@400;700&family=Raleway:wght@300&display=swap">
<style>
  :root {
    --backdrop: #2b1213;
    --card: #ffffff;
    --teal: #45b99f;
    --teal-text: #3aa88e;
    --teal-deep: #4a9284;
    --white: #ffffff;
  }
  * { margin: 0; padding: 0; box-sizing: border-box; }
  html, body {
    width: 1200px; height: 800px; overflow: hidden;
    background: var(--backdrop);
  }
  .stage {
    width: 1200px; height: 800px;
    display: flex; align-items: center; justify-content: center;
  }
  .card {
    position: relative;
    width: 900px; height: 514px;
    background: var(--card);
    overflow: hidden;
    font-family: "Arimo", Arial, sans-serif;
    color: var(--teal-text);
  }
  .card__band {
    position: absolute; left: 0; right: 0; bottom: 0; height: 250px;
    background: linear-gradient(to bottom, rgba(255,255,255,0) 0%, rgba(168,210,200,0.35) 45%, var(--teal-deep) 100%);
  }
  .brand {
    position: absolute; left: 64px; top: 178px;
    display: flex; align-items: center; gap: 30px;
  }
  .brand__dot {
    width: 118px; height: 118px; border-radius: 50%;
    background: var(--teal);
    flex: none;
  }
  .brand__text { display: flex; flex-direction: column; gap: 6px; }
  .brand__name {
    font-size: 50px; line-height: 56px; font-weight: 400;
    color: var(--teal-text); letter-spacing: 0.5px;
  }
  .brand__tagline {
    font-size: 14px; line-height: 18px; font-weight: 400;
    color: var(--teal-text); white-space: nowrap;
  }
  .contact {
    position: absolute; left: 480px; top: 78px;
    font-size: 19px; line-height: 24px;
  }
  .contact__name { font-weight: 700; font-size: 22px; }
  .contact__role { padding-left: 18px; }
  .contact__phones { margin-top: 26px; padding-left: 40px; }
  .contact__web { margin-top: 26px; padding-left: 80px; }
  .card__url {
    position: absolute; left: 38px; bottom: 26px;
    font-family: "Raleway", Arial, sans-serif; font-weight: 300;
    font-size: 46px; color: var(--white); letter-spacing: 1px;
  }
</style>
</head>
<body>
  <main class="stage">
    <article class="card">
      <div class="card__band" role="img" aria-label="Soft teal band with faint binary digit pattern"></div>

      <div class="brand">
        <div class="brand__dot"></div>
        <div class="brand__text">
          <div class="brand__name">Vyrolux</div>
          <div class="brand__tagline">the new normal cloud video management</div>
        </div>
      </div>

      <div class="contact">
        <div class="contact__name">Daniel Moraw</div>
        <div class="contact__role">Founder</div>
        <div class="contact__phones">
          <div>tel.: +1.555.014.2290</div>
          <div>fax: +1.555.014.7731</div>
        </div>
        <div class="contact__web">
          <div>info@vyrolux.me</div>
          <div>www.vyrolux.me</div>
        </div>
      </div>

      <div class="card__url">www.vyrolux.me</div>
    </article>
  </main>
</body>
</html>
```